VFX Company Business Card Design Project

The Ember Vale is a decentralized Visual Effects Studio servicing the television and feature film industries.
Project Brief:
Take our logo that was previously designed on Pixel Harbor and make a double sided business card.
Requirements:
- Card MUST be double sided.
- Front of card MUST have the yellow part of our logo against the dark grey background.
- Back of card is completely up to the designer.
- Back of card must include the complete company logo.
Please follow these File Preparation guidelines:
http://printmoor.example/infopage?file=filetype_en&s=PrintMoor_new&lang=en
Industry/Entity Type
Business
Look and feel
Each slider illustrates characteristics of the customer's brand and the style your logo design should communicate.

```html
<!DOCTYPE html>
<html lang="en">
<head>
<meta charset="utf-8">
<title>The Ember Vale — Business Cards</title>
<link rel="stylesheet" href="https://fonts.googleapis.com/css2?family=Merriweather:wght@300;400;700&display=swap">
<style>
  :root {
    --card-yellow: #fdc928;
    --card-charcoal: #2f2f2f;
    --ink-dark: #4a4a4a;
    --ink-muted: #7d6a2a;
    --ink-light: #ffffff;
    --backdrop: #ebe8e3;
    --corner: 34px;
  }
  * { margin: 0; padding: 0; box-sizing: border-box; }
  html, body { width: 998px; height: 1200px; overflow: hidden; }
  body {
    background: var(--backdrop);
    font-family: "Merriweather", Georgia, serif;
    position: relative;
  }
  .card {
    position: absolute;
    border-radius: 0 var(--corner) 0 var(--corner);
    box-shadow: 0 6px 18px rgba(0,0,0,0.18);
  }
  .card--front { background: var(--card-yellow); }
  .card--back { background: var(--card-charcoal); }

  .card--portrait { width: 340px; height: 566px; top: 50px; }
  .card--landscape { width: 440px; height: 264px; top: 700px; }

  .wordmark {
    display: flex; align-items: center; gap: 8px;
    font-weight: 700; font-size: 17px; color: var(--ink-light);
    white-space: nowrap;
  }
  .wordmark__dot {
    width: 14px; height: 14px; border-radius: 50%;
    background: var(--ink-light);
  }

  .details { color: var(--ink-dark); font-weight: 300; font-size: 15px; line-height: 1.25; }
  .details__name { font-size: 20px; font-weight: 400; }
  .details__role { font-size: 14px; color: var(--ink-muted); }
  .details__address { margin-top: 26px; }
  .details__contacts { margin-top: 30px; color: var(--ink-light); }
  .details__contacts b { font-weight: 700; }
  .details__web { margin-top: 24px; color: var(--ink-light); }

  /* portrait front */
  .front-portrait .wordmark { position: absolute; top: 52px; right: 38px; }
  .front-portrait .details { position: absolute; right: 38px; top: 305px; text-align: right; }

  /* landscape front */
  .front-landscape .details { position: absolute; left: 38px; top: 34px; font-size: 13px; }
  .front-landscape .details__name { font-size: 17px; }
  .front-landscape .details__role { font-size: 12px; }
  .front-landscape .details__address { margin-top: 20px; }
  .front-landscape .details__contacts { margin-top: 22px; }
  .front-landscape .details__web { margin-top: 20px; }
  .front-landscape .wordmark { position: absolute; right: 38px; bottom: 42px; font-size: 15px; }

  /* back sides */
  .back-mark {
    position: absolute; display: flex; align-items: center; gap: 14px;
    color: var(--card-yellow); font-weight: 700; white-space: nowrap;
  }
  .back-mark__dot { border-radius: 50%; background: var(--card-yellow); }
  .back-portrait .back-mark { left: 36px; bottom: 50px; font-size: 30px; }
  .back-portrait .back-mark__dot { width: 26px; height: 26px; }
  .back-landscape .back-mark { left: 50%; top: 50%; transform: translate(-50%, -50%); font-size: 30px; }
  .back-landscape .back-mark__dot { width: 26px; height: 26px; }
</style>
</head>
<body>

  <section class="card card--front card--portrait front-portrait" style="left:139px">
    <div class="wordmark"><span class="wordmark__dot"></span>The Ember Vale</div>
    <div class="details">
      <p class="details__name">Mara Lindqvist</p>
      <p class="details__role">VFX Artist</p>
      <p class="details__address">Harbor Lane<br>Suite 210</p>
      <p class="details__contacts"><b>phone</b> : +001 555 014229<br><b>email</b> : hi@embervale.example<br><b>fax</b> : +01 5550173384</p>
      <p class="details__web">www.embervale.example</p>
    </div>
  </section>

  <section class="card card--back card--portrait back-portrait" style="left:519px">
    <div class="back-mark"><span class="back-mark__dot"></span>The Ember Vale</div>
  </section>

  <section class="card card--front card--landscape front-landscape" style="left:39px">
    <div class="details">
      <p class="details__name">Mara Lindqvist</p>
      <p class="details__role">VFX Artist</p>
      <p class="details__address">Harbor Lane<br>Suite 210</p>
      <p class="details__contacts"><b>phone</b> : +001 555 014229<br><b>email</b> : hi@embervale.example<br><b>fax</b> : +01 5550173384</p>
      <p class="details__web">www.embervale.example</p>
    </div>
    <div class="wordmark"><span class="wordmark__dot"></span>The Ember Vale</div>
  </section>

  <section class="card card--back card--landscape back-landscape" style="left:519px">
    <div class="back-mark"><span class="back-mark__dot"></span>The Ember Vale</div>
  </section>

</body>
</html>
```